Fitness business need 3x3 card to promote 6wk boot camp nutrition challenge

Hi, we're looking for someone to make our current card look better and more modern. We want to keep the text the same, but we want a better design. We also want to keep the woman on the front of the card. The card is for both men and women so we want it to feel inclusive and bright. The idea is to make the card look more modern. We want some pops of color. The main feature is to promote the pricing on the back of the card. It would be nice if that continues to look like a coupon or if it stands out with a bright color or background.

Target Market(s)

Men and women looking to get in shape

Industry/Entity Type

Fitness

Font styles to use
Serif
Sans Serif

Colors
3176b5
0255a3
33a6d7
f37122
ec1f27

Requirements
Must have
• front and back, use pic of women provided

```html
<!DOCTYPE html>
<html lang="en">
<head>
<meta charset="utf-8">
<title>Fitness Boot Camp Card</title>
<link rel="stylesheet" href="https://fonts.googleapis.com/css2?family=Michroma&family=Roboto:wght@300;400;700&display=swap">
<style>
  :root {
    --canvas-bg: #e6e3de;
    --charcoal: #545658;
    --charcoal-deep: #47494b;
    --fold: #353739;
    --steel: #8c8e90;
    --steel-dark: #6e7072;
    --steel-right: #7b7d7f;
    --paper-light: #f5f5f3;
    --paper-shade: #d6d7d7;
    --ink: #3a3b3d;
    --cyan: #3fb4dc;
    --orange: #f37122;
    --white: #ffffff;
  }
  * { box-sizing: border-box; margin: 0; padding: 0; }
  html, body { width: 1200px; height: 1000px; overflow: hidden; }
  body { background: var(--canvas-bg); position: relative; font-family: "Roboto", Arial, sans-serif; }

  .card {
    position: absolute; left: 50px; top: 50px; width: 1100px; height: 900px;
    background: radial-gradient(ellipse at 50% 40%, var(--paper-light) 0%, #ebebea 45%, var(--paper-shade) 100%);
    overflow: hidden;
    box-shadow: 0 6px 24px rgba(0,0,0,.18);
  }
  .card > * { position: absolute; }

  .rule { left: 0; width: 100%; background: var(--charcoal); }
  .rule--top { top: 11px; height: 12px; }
  .rule--under-a { top: 178px; height: 8px; background: var(--steel); }
  .rule--under-b { top: 198px; height: 11px; }

  .header { top: 31px; left: 0; width: 100%; height: 140px; background: var(--charcoal); text-align: center; }
  .header__title {
    font-family: "Michroma", sans-serif; color: var(--white); font-weight: 400;
    font-size: 56px; line-height: 1; letter-spacing: 1px; padding-top: 20px; white-space: nowrap;
  }
  .header__subtitle {
    font-family: "Michroma", sans-serif; color: var(--cyan);
    font-size: 28px; line-height: 1; margin-top: 24px; white-space: nowrap;
  }

  .alert-band {
    top: 220px; left: 0; width: 100%; height: 70px; background: var(--charcoal);
    color: var(--orange); font-family: "Michroma", sans-serif; font-size: 30px;
    display: flex; align-items: center; justify-content: center; word-spacing: 10px; white-space: nowrap;
  }

  .pitch {
    top: 310px; left: 0; width: 100%; text-align: center;
    color: var(--ink); font-weight: 300; font-size: 37px; line-height: 39px;
  }

  .cta {
    top: 450px; left: 253px; width: 600px; height: 90px;
    background: var(--charcoal); border-radius: 12px; color: var(--white);
    font-family: "Michroma", sans-serif; font-size: 46px; white-space: nowrap;
    display: flex; align-items: center; justify-content: center;
  }
  .cta__rivet { position: absolute; width: 9px; height: 9px; border-radius: 50%; background: #c9cacb; }
  .cta__rivet--tl { top: 10px; left: 10px; }
  .cta__rivet--tr { top: 10px; right: 10px; }
  .cta__rivet--bl { bottom: 10px; left: 10px; }
  .cta__rivet--br { bottom: 10px; right: 10px; }

  .price-band {
    top: 601px; left: 0; width: 100%; height: 146px;
    background: linear-gradient(90deg, var(--steel-dark), var(--steel) 40%);
  }
  .price-tag { top: 574px; left: 0; width: 1100px; height: 201px; }
  .price-band__label {
    top: 610px; left: 43px; color: var(--white); font-weight: 700;
    font-size: 54px; line-height: 64px; white-space: nowrap;
  }
  .price-tag__amount {
    top: 574px; left: 515px; width: 500px; height: 201px;
    display: flex; align-items: center; justify-content: center;
    color: var(--orange); font-weight: 700; font-size: 150px; line-height: 1;
  }

  .contact {
    top: 776px; left: 20px; width: 400px; text-align: center; font-style: normal;
    color: var(--ink); font-weight: 700; font-size: 31px; line-height: 35px; white-space: nowrap;
  }

  .brand {
    top: 800px; left: 600px; width: 400px; height: 80px;
    display: flex; align-items: center; justify-content: center; gap: 14px;
  }
  .brand__dot { width: 22px; height: 22px; border-radius: 50%; background: var(--charcoal); flex: none; }
  .brand__name { color: var(--charcoal); font-weight: 700; font-size: 32px; letter-spacing: 1px; white-space: nowrap; }
</style>
</head>
<body>
  <main class="card">
    <div class="rule rule--top"></div>

    <header class="header">
      <h1 class="header__title">Fitness Boot Camp</h1>
      <p class="header__subtitle">6 Week Fitness &amp; Nutrition Boot Camp</p>
    </header>

    <div class="rule rule--under-a"></div>
    <div class="rule rule--under-b"></div>

    <p class="alert-band">NO BARBELLS! NO HEAVY WEIGHTS!</p>

    <p class="pitch">
      Burn fat, build muscle &amp; have fun!<br>
      Tons of classes led by world-class coaches.<br>
      Personalized nutrition planning, prizes, and more!
    </p>

    <div class="cta">
      <span class="cta__rivet cta__rivet--tl"></span>
      <span class="cta__rivet cta__rivet--tr"></span>
      <span class="cta__rivet cta__rivet--bl"></span>
      <span class="cta__rivet cta__rivet--br"></span>
      Sign up Today!
    </div>

    <div class="price-band"></div>
    <svg class="price-tag" viewBox="0 0 1100 201" aria-hidden="true">
      <polygon points="489,27 515,0 515,27" fill="#353739"/>
      <rect x="515" y="0" width="500" height="201" fill="#47494b"/>
      <rect x="1015" y="27" width="85" height="146" fill="#7b7d7f"/>
      <polygon points="1015,173 1040,173 1015,201" fill="#353739"/>
    </svg>
    <p class="price-band__label">6 WEEKS<br>FOR ONLY</p>
    <p class="price-tag__amount">$249</p>

    <address class="contact">
      555-012-3488<br>
      42 Harbor Lane<br>
      Millbrook, OH 44012
    </address>

    <div class="brand">
      <span class="brand__dot"></span>
      <span class="brand__name">PEAKFORM CAMP</span>
    </div>
  </main>
</body>
</html>
```